Start-Up Property Development Company Requires Word Press Website Design

A new property development company in Sydney requires a new website.
This version (Version 1) is very simple and will represent one, small aspect of what the company does, which is acquiring properties for redevelopment:

Needed:
- 1 page incorporating copy, logo and illustration.
- Email contact form.
- Contact information.

It will be expanded in the next few months to include another section for marketing homes for sale (Version 2). This section should sit on top of the Version 1 (in the top section of the same scrolling page).

So this initial design must be able to simply incorporate the expansion.

The site design needs to:
- Take up the entire width of the monitor.
- Not be too different from companies corporate look and feel.
- Be simple, functional and elegant.
- Have a long scroll (1 page) with navigation items at the top of the screen simply linking to the corresponding section lower in the page.

Reason: Not happy with the choice of designs. I'm wanting something clean and fresh and not too intensive with graphics.

```html
<!DOCTYPE html>
<html lang="en">
<head>
<meta charset="utf-8">
<title>Harbourline Property</title>
<link href="https://fonts.googleapis.com/css2?family=Roboto+Condensed:wght@400;700&family=Roboto:wght@400;700&display=swap" rel="stylesheet">
<style>
:root{
  --red:#d0232a;
  --red-band:#c62a2f;
  --red-footer:#b52127;
  --dark:#232323;
  --ink:#222;
  --grey:#555;
  --line:#ddd;
}
*{margin:0;padding:0;box-sizing:border-box}
html,body{width:918px;height:1200px;overflow:hidden;background:#fff}
body{position:relative;font-family:Roboto,Arial,sans-serif;color:var(--ink)}
.abs{position:absolute}
.cond{font-family:"Roboto Condensed",Arial,sans-serif}

/* header */
.header{left:0;top:0;width:918px;height:105px;background:#fff;border-bottom:1px solid #e5e5e5}
.brand{left:60px;top:24px;display:flex;align-items:center;gap:8px}
.brand-mark{width:22px;height:22px;background:var(--red)}
.brand-name{font-family:"Roboto Condensed",sans-serif;font-weight:700;font-size:27px;color:var(--ink);letter-spacing:.5px;line-height:1}
.brand-tag{left:74px;top:80px;font-size:9.5px;color:var(--ink)}
.topcall{left:705px;top:14px;display:flex;gap:7px;align-items:center}
.topcall small{display:block;font-size:12px}
.topcall strong{display:block;font-family:"Roboto Condensed",sans-serif;font-weight:400;font-size:23px;line-height:1}
.nav{left:438px;top:68px;display:flex;gap:0}
.nav a{font-family:"Roboto Condensed",sans-serif;font-size:14px;color:var(--ink);text-decoration:none;padding:4px 13px;margin-right:2px}
.nav a.active{background:var(--red);color:#fff}

/* hero */
.hero{left:0;top:105px;width:918px;height:304px;background:linear-gradient(180deg,#8a6fa6 0%,#a679a6 40%,#cf8f9e 62%,#6b5a5e 80%,#3b3332 100%)}
.hero-caption{left:120px;top:365px;width:580px;height:34px;background:rgba(30,30,30,.45);color:#fff;font-size:26px;text-align:center;line-height:34px}
.band{left:0;top:409px;width:918px;height:81px;background:var(--dark)}
.band p{position:absolute;left:51px;top:15px;color:#fff;font-family:"Roboto Condensed",sans-serif;font-weight:700;font-size:19.5px;line-height:23px;width:600px}
.band-call{left:676px;top:422px;width:190px;height:54px;background:var(--red);border-radius:3px;color:#fff;text-align:center;font-family:"Roboto Condensed",sans-serif}
.band-call span{display:block;font-size:19px;padding-top:4px;line-height:22px}
.band-call b{display:block;font-size:25px;line-height:26px}

/* sections */
.h2{font-family:"Roboto Condensed",sans-serif;font-weight:700;font-size:20px;color:var(--ink)}
.h2 em{font-style:normal;color:var(--red)}
.rule{height:0;border-top:2px dotted #e2e2e2}
.rule.yellow{border-top-color:#f3ebb6}
.service{width:220px;text-align:center}
.service h3{font-family:"Roboto Condensed",sans-serif;font-weight:400;font-size:18px;line-height:18px;margin-top:10px}
.service.residential h3{color:var(--red)}
.service p{font-size:11.3px;color:var(--grey);line-height:15.5px;margin:16px auto 0;width:200px}
.vdivider{left:552px;top:545px;width:1px;height:195px;background:#eee}
.field{left:576px;width:246px;border:1px solid #ccc;border-radius:3px;font-size:11px;font-style:italic;color:#777;padding:6px 10px;background:#fff}
.btn{height:22px;background:var(--red);color:#fff;font-family:"Roboto Condensed",sans-serif;font-size:15px;text-align:center;line-height:22px;border-radius:2px}
.soft-line{left:70px;top:756px;width:780px;height:2px;background:linear-gradient(90deg,transparent,#eee,transparent)}
.welcome-text{left:61px;top:826px;width:522px;font-size:11.3px;line-height:19px;color:var(--grey)}
.welcome-text a{color:var(--red);font-weight:700;text-decoration:none}
.callme{left:61px;top:929px;font-family:"Roboto Condensed",sans-serif;font-size:22px;line-height:26px;color:#555}
.callme span{color:var(--red)}
.illustration{left:640px;top:800px;width:235px;height:150px;background:radial-gradient(circle at 40% 50%,#b7d49a,#7fae6a 50%,#e9ede4 80%)}

/* value band + footer */
.value{left:0;top:984px;width:918px;height:79px;background:var(--red-band);color:#fff;font-size:15.5px;line-height:20px;text-align:center;padding:10px 66px}
.footer{left:0;top:1063px;width:918px;height:137px;background:var(--red-footer);color:#fff}
.fnav{left:50px;top:1078px;display:flex;gap:17px;font-size:12.5px}
.fnav .active{color:#2a0a0a}
.fline{left:50px;top:1104px;width:470px;border-top:1px dashed rgba(255,255,255,.4)}
.faddr{left:50px;top:1115px;font-size:12.3px}
.fcontact{left:50px;top:1141px;font-size:12.3px;display:flex;gap:0}
.fcontact b{font-size:14px;font-weight:400;margin-right:10px}
.copyright{left:51px;top:1176px;font-size:11px}
.subscribe{left:676px;top:1075px;font-size:13px;font-weight:700;letter-spacing:.2px}
.sub-field{left:674px;top:1098px;width:177px;height:26px;background:#d98a8c;border:1px solid #e4a9aa;font-size:11px;font-style:italic;color:#fff;padding:6px 10px}
.sub-btn{left:675px;top:1135px;width:62px;height:22px;background:#111;color:#fff;font-family:"Roboto Condensed",sans-serif;font-size:14px;text-align:center;line-height:22px}
.social{top:1170px;width:22px;height:22px;border-radius:3px;background:rgba(255,255,255,.85)}
</style>
</head>
<body>

<header class="abs header">
  <div class="abs brand"><span class="brand-mark"></span><span class="brand-name">HARBOURLINE PROPERTY</span></div>
  <div class="abs brand-tag">Residential &amp; Commercial Development</div>
  <div class="abs topcall">
    <svg width="28" height="28" viewBox="0 0 28 28"><circle cx="14" cy="14" r="12.5" fill="none" stroke="#d0232a" stroke-width="2"/><path d="M10 8c-1 1-1 3 0 5s3 5 5 6 3 1 4 0l-2-3-2 1c-1-1-2-2-3-4l1-2z" fill="#d0232a"/></svg>
    <div><small>Call Us Today</small><strong>02 9000 4821</strong></div>
  </div>
  <nav class="abs nav">
    <a class="active" href="#home">HOME</a><a href="#about">ABOUT US</a><a href="#services">SERVICES</a><a href="#gallery">WORK GALLERY</a><a href="#contact">CONTACT US</a>
  </nav>
</header>

<section class="abs hero" role="img" aria-label="Sydney city skyline at dusk under a purple sky"></section>
<div class="abs hero-caption cond">We Acquire And Redevelop Properties In Sydney</div>
<svg class="abs" style="left:52px;top:218px" width="42" height="42" viewBox="0 0 42 42"><circle cx="21" cy="21" r="19" fill="#111" stroke="#555" stroke-width="3"/><path d="M24 13l-8 8 8 8" fill="none" stroke="#fff" stroke-width="1.5"/></svg>
<svg class="abs" style="left:825px;top:218px" width="42" height="42" viewBox="0 0 42 42"><circle cx="21" cy="21" r="19" fill="#111" stroke="#555" stroke-width="3"/><path d="M18 13l8 8-8 8" fill="none" stroke="#fff" stroke-width="1.5"/></svg>

<div class="abs band"><p>So if you’re thinking of selling or interested in knowing what we think your property is worth, please contact us!</p></div>
<div class="abs band-call"><span>Call Us Today</span><b>02 9000 4821</b></div>

<section id="services">
  <h2 class="abs h2" style="left:62px;top:513px">What We <em>D</em>o</h2>
  <div class="abs rule" style="left:62px;top:539px;width:465px"></div>
  <svg class="abs" style="left:108px;top:558px" width="78" height="60" viewBox="0 0 78 60"><path d="M39 2L2 34h8v26h58V34h8z" fill="#d0232a"/><rect x="14" y="38" width="9" height="9" fill="#fff"/><rect x="28" y="38" width="9" height="9" fill="#fff"/><rect x="55" y="38" width="9" height="9" fill="#fff"/><rect x="42" y="40" width="9" height="20" fill="#fff"/><path d="M39 10L10 34" stroke="#fff" stroke-width="2"/><path d="M39 10l29 24" stroke="#fff" stroke-width="2"/></svg>
  <svg class="abs" style="left:378px;top:560px" width="59" height="57" viewBox="0 0 59 57"><rect x="25" y="0" width="28" height="53" fill="#222"/><rect x="3" y="18" width="24" height="35" fill="#222"/><rect x="0" y="52" width="59" height="5" fill="#222"/><g fill="#fff"><rect x="30" y="5" width="5" height="5"/><rect x="40" y="5" width="5" height="5"/><rect x="30" y="15" width="5" height="5"/><rect x="40" y="15" width="5" height="5"/><rect x="30" y="25" width="5" height="5"/><rect x="40" y="25" width="5" height="5"/><rect x="30" y="35" width="5" height="5"/><rect x="40" y="35" width="5" height="5"/><rect x="8" y="24" width="5" height="5"/><rect x="17" y="24" width="5" height="5"/><rect x="8" y="34" width="5" height="5"/><rect x="17" y="34" width="5" height="5"/><rect x="8" y="44" width="5" height="5"/><rect x="17" y="44" width="5" height="5"/></g></svg>
  <div class="abs service residential" style="left:37px;top:625px"><h3>Residential<br>Project Development</h3><p>Lorem ipsum dolor sit amet, consectetuer adipiscing elit, sed diam nonummy nibh</p></div>
  <div class="abs service" style="left:296px;top:625px"><h3>Industrial<br>Project Development</h3><p>Lorem ipsum dolor sit amet, consectetuer adipiscing elit, sed diam nonummy nibh</p></div>
</section>

<div class="abs vdivider"></div>

<section id="contact">
  <h2 class="abs h2" style="left:574px;top:513px">Quick Contact</h2>
  <div class="abs rule yellow" style="left:574px;top:539px;width:246px"></div>
  <div class="abs field" style="top:553px;height:26px">Name</div>
  <div class="abs field" style="top:587px;height:25px">Email</div>
  <div class="abs field" style="top:621px;height:73px">Message</div>
  <div class="abs btn" style="left:577px;top:702px;width:62px">Submit</div>
</section>

<div class="abs soft-line"></div>

<section id="about">
  <h2 class="abs h2" style="left:61px;top:780px">Welcome to <em>H</em>arbourline Property</h2>
  <div class="abs rule" style="left:61px;top:812px;width:519px"></div>
  <p class="abs welcome-text">Lorem ipsum dolor sit amet, consectetuer adipiscing elit, sed diam nonummy nibh euis loremod tincidunt ut laoreet dolore magna aliquam erat volutpat. Ut wisi enim ad minim veniam, quis rore nostrud exerci tation ullamcorper suscipit lobortis nisl ut aliquip ex ea commodo consequat. Dui autem vel eum iriure dolor in hendrerit in vulputate velit esse molestie consequat, vel illum lorem dolore eu feugiat nulla facilisis at vero eros et accumsan et iusto odi<a href="#about">.....Read More</a></p>
  <p class="abs callme">If you have any questions, please call me at <span>02 9000 4821</span></p>
  <div class="abs illustration" role="img" aria-label="Model house made of banknotes under a magnifying glass"></div>
</section>

<div class="abs value">We value properties using their potential value following redevelopment, rather than the commonly used methods of recent, comparative sales and the opinions of agents.Because of this we can sometimes offer more than what is typical for your local market.</div>

<footer class="abs footer"></footer>
<nav class="abs fnav" style="color:#fff"><span class="active">HOME</span><span>ABOUT US</span><span>SERVICES</span><span>WORK GALLERY</span><span>CONTACT US</span></nav>
<div class="abs fline"></div>
<p class="abs faddr" style="color:#fff">Harbourline Pty Ltd., P.O. Box 12, Surry Hills NSW 2010</p>
<p class="abs fcontact" style="color:#fff"><b>P:</b><span style="font-weight:700;margin-right:24px">02 9000 4821</span><b>TF:</b><span style="margin-right:22px">0410 000 372</span><b>E:</b><span>info@harbourline.com.au</span></p>
<p class="abs copyright" style="color:#fff">Copyright ©2014 HarbourlineProperty &nbsp;All Rights Reserved</p>
<p class="abs subscribe" style="color:#fff">Subscribe to Newsletter</p>
<div class="abs sub-field">Email here</div>
<div class="abs sub-btn">Submit</div>
<span class="abs social" style="left:677px"></span>
<span class="abs social" style="left:707px"></span>
<span class="abs social" style="left:737px"></span>
<span class="abs social" style="left:767px"></span>

</body>
</html>
```